Restaurant needs a vertical banner for fried catfish

Our restaurant is looking for an eye-catching 78.75in. x 36in. vertical physical banner ad for our fried catfish. Photos for the fried catfish will be provided as a reference but we will also accept anything similar to the photo. We will be using the following as our receptacle: https://www.plankoria.example/banner-stand/retractable-banner-stands/
The design must incorporate the following flavor texts:
Fried Catfish
Always Fresh!
Made from Scratch
Hand-cut Fillets
The Best Catfish in Texas
Served with fries, hush puppies, and a 32oz fountain drink
Also available by the pound!
The final design should be creative, professional, and eye-catching for customers.
Updates
Colors
Designer to choose colors to be used in the design.
Requirements
Must have
- We are open to any and all design elements, albeit the 'flavor texts' should not overpower, but complement the fried catfish photo. 'Fried Catfish' can be used in lieu of a main title/logo.
Nice to have
- Transparent or textured backgrounds that can encompass any or all part of the banner such as a cutting board, shadows, abstract, etc to show depth are a plus.
- Use of vectors or objects such as ribbons or shapes to encapsulate the 'flavor texts' are also encouraged.

```html
<!DOCTYPE html>
<html lang="en">
<head>
<meta charset="utf-8">
<title>Fried Catfish Banner</title>
<link rel="stylesheet" href="https://fonts.googleapis.com/css2?family=Comfortaa:wght@600;700&display=swap">
<style>
  :root {
    --page: #ffffff;
    --banner-brown: #b5732e;
    --badge-orange: #f6a22b;
    --band-white: #ffffff;
    --band-text: #f0961f;
    --text-white: #ffffff;
    --photo-deep: #a8641f;
    --photo-light: #e0a556;
  }
  * { margin: 0; padding: 0; box-sizing: border-box; }
  html, body {
    width: 1200px; height: 1200px; overflow: hidden;
    background: var(--page);
  }
  .canvas {
    position: relative; width: 1200px; height: 1200px;
    font-family: "Comfortaa", sans-serif;
  }
  .banner {
    position: absolute; left: 340px; top: 30px;
    width: 524px; height: 1140px;
    background: var(--banner-brown);
  }
  .title {
    position: absolute; left: 0; top: 78px; width: 100%;
    padding-left: 40px;
    text-align: center; color: var(--text-white);
    font-size: 66px; font-weight: 700; letter-spacing: 0.5px;
    line-height: 1;
  }
  .dish-photo {
    position: absolute; left: 11px; top: 216px;
    width: 500px; height: 350px; border-radius: 50%;
    background: radial-gradient(ellipse at 55% 45%, var(--photo-light) 0%, var(--photo-deep) 75%);
  }
  .badge {
    position: absolute; border-radius: 50%;
    background: var(--badge-orange); color: var(--text-white);
    display: flex; align-items: center; justify-content: center;
    text-align: center; font-weight: 700; line-height: 1.0;
  }
  .badge-fresh   { left: 9px;   top: 590px; width: 233px; height: 115px; font-size: 34px; }
  .badge-handcut { left: 273px; top: 590px; width: 235px; height: 113px; font-size: 34px; }
  .badge-scratch { left: 9px;   top: 742px; width: 233px; height: 125px; font-size: 34px; }
  .badge-best    { left: 269px; top: 736px; width: 235px; height: 125px; font-size: 31px; }
  .badge-served  { left: 52px;  top: 894px; width: 413px; height: 125px; font-size: 26px; line-height: 1.08; }
  .pound-band {
    position: absolute; left: 0; top: 1050px; width: 100%; height: 78px;
    background: var(--band-white); color: var(--band-text);
    display: flex; align-items: center; justify-content: center;
    padding-right: 40px;
    text-align: center; font-size: 32px; font-weight: 700; line-height: 1.12;
  }
</style>
</head>
<body>
<div class="canvas">
  <section class="banner">
    <h1 class="title">Fried Catfish</h1>
    <div class="dish-photo" role="img" aria-label="Photo of golden fried catfish fillets with fries and hush puppies on a plate"></div>
    <div class="badge badge-fresh">Always<br>Fresh!</div>
    <div class="badge badge-handcut">Hand-cut<br>Fillets</div>
    <div class="badge badge-scratch">Made from<br>Scratch</div>
    <div class="badge badge-best">The<br>Best Catfish<br>in Texas</div>
    <div class="badge badge-served">Served with fries, hush<br>puppies, and a 32oz<br>fountain drink</div>
    <div class="pound-band">Also available by<br>the pound!</div>
  </section>
</div>
</body>
</html>
```